Front page on www.brightlanegoods.com modern service ads - each ad for each featured service

We need to have initial 5 banners to be created for our soon to be launched new site,. These are 5 rotating banners that will showcase our companies key features. We are looking for a modern stylish yet simple look to highlight these features. Something thats very inviting and modern to fit the look of the new website.

5 banners need to be, information can be found on www.brightlanegoods.com about these. Please ask if any questions

Why us?
Art Services
Order Process
Current promotions
Clearance products

please also note. the design will be going onto this website. http://new.brightlanegoods.com/ Please base actual designs , color schemes etc.. for the new site.

Target Market(s)

Small businesses that purchase marketing promotional goods, to promote their business

Industry/Entity Type

Promotional Product

Font styles to use
Sans Serif

Requirements
Must have
• Size of the banner is 965 x 400 px
Nice to have
• Modern elements,, very clean and minimal look
Should not have
• no cheap generic clip art

```html
<!DOCTYPE html>
<html lang="en">
<head>
<meta charset="utf-8">
<title>Current Promotions – Bright Lane Goods</title>
<link rel="stylesheet" href="https://fonts.googleapis.com/css2?family=Montserrat:ital,wght@1,700;1,800&display=swap">
<style>
  :root {
    --navy: #2c3263;
    --periwinkle: #8e99d6;
    --lilac: #d8d0f4;
    --white: #ffffff;
  }
  html, body {
    margin: 0;
    padding: 0;
    width: 1200px;
    height: 497px;
    overflow: hidden;
    background: var(--white);
  }
  .banner {
    display: block;
    width: 1200px;
    height: 497px;
  }
  .headline {
    font-family: "Montserrat", Arial, sans-serif;
    font-style: italic;
    font-weight: 800;
    fill: var(--white);
  }
  .subline {
    font-family: "Montserrat", Arial, sans-serif;
    font-style: italic;
    font-weight: 700;
    fill: var(--white);
  }
  .tagline {
    font-family: "Montserrat", Arial, sans-serif;
    font-style: italic;
    font-weight: 700;
    fill: var(--white);
  }
  .blob { fill: var(--periwinkle); }
  .accent-navy { fill: var(--navy); }
  .accent-lilac { fill: var(--lilac); }
  .ring { fill: none; stroke: var(--periwinkle); stroke-width: 1.5; }
  .plus { stroke: var(--periwinkle); stroke-width: 1.5; }
  .bracket { fill: none; stroke: var(--navy); stroke-width: 4; }
  .dots { fill: var(--lilac); }
</style>
</head>
<body>
<svg class="banner" viewBox="0 0 965 400" xmlns="http://www.w3.org/2000/svg">
  <defs>
    <pattern id="dot-grid" width="7" height="7" patternUnits="userSpaceOnUse">
      <circle cx="2" cy="2" r="1.2" class="dots"/>
    </pattern>
    <linearGradient id="product-tone" x1="0" y1="0" x2="1" y2="1">
      <stop offset="0" stop-color="#f3f4f6"/>
      <stop offset="0.6" stop-color="#e6e8ee"/>
      <stop offset="1" stop-color="#cfd3e3"/>
    </linearGradient>
  </defs>

  <!-- background shapes -->
  <path class="blob" d="M0 0 H560 C520 40 470 30 430 15 C380 0 330 -5 280 25 C230 55 200 30 160 25 C110 18 70 40 55 80 C40 120 60 160 40 200 C30 230 10 250 0 260 Z"/>
  <path class="blob" d="M965 60 C930 80 900 110 905 160 C910 220 880 250 840 270 C790 295 760 330 700 345 C640 360 600 380 570 400 H965 Z"/>
  <path class="accent-navy" d="M842 0 H905 L865 48 Z"/>

  <!-- floating accents -->
  <circle class="accent-navy" cx="136" cy="130" r="19"/>
  <path class="accent-navy" d="M93 332 L160 268 L168 360 Z"/>
  <path class="accent-lilac" d="M528 88 L600 18 L615 90 Z"/>
  <circle class="accent-lilac" cx="636" cy="74" r="16"/>
  <circle class="accent-lilac" cx="345" cy="370" r="14"/>
  <circle class="accent-navy" cx="745" cy="112" r="17"/>
  <circle class="accent-navy" cx="642" cy="262" r="17"/>
  <circle class="ring" cx="230" cy="150" r="5"/>
  <circle class="ring" cx="680" cy="78" r="5"/>
  <circle class="ring" cx="430" cy="360" r="4"/>
  <path class="plus" d="M292 42 v10 M287 47 h10"/>
  <path class="plus" d="M676 130 v10 M671 135 h10"/>
  <path class="plus" d="M280 376 v10 M275 381 h10"/>
  <rect x="470" y="220" width="210" height="120" fill="url(#dot-grid)" opacity="0.8"/>

  <!-- corner frame -->
  <path class="bracket" d="M206 58 V37 H227"/>
  <path class="bracket" d="M688 37 H709 V58"/>
  <path class="bracket" d="M206 362 V383 H227"/>
  <path class="bracket" d="M688 383 H709 V362"/>

  <!-- headline ribbons -->
  <path class="blob" d="M268 73 H482 L474 108 H258 Z"/>
  <path class="accent-navy" d="M248 108 H600 C640 108 650 150 620 165 C650 180 660 230 620 240 L590 290 H238 Z"/>
  <path class="blob" d="M238 286 H420 L410 320 H232 Z" opacity="0.95"/>
  <path class="accent-navy" d="M560 150 H665 C690 150 690 185 665 185 H560 Z" opacity="0"/>

  <text class="headline" x="432" y="174" font-size="39" text-anchor="middle">CURRENT</text>
  <text class="headline" x="432" y="222" font-size="39" text-anchor="middle">PROMOTIONS</text>
  <text class="subline" x="432" y="257" font-size="16" text-anchor="middle">STELLAR DEALS STARTING FROM $1</text>

  <!-- tagline pill -->
  <path class="blob" d="M385 296 H612 C624 296 626 306 622 316 L612 344 C609 350 604 352 598 352 H372 Z"/>
  <line x1="300" y1="288" x2="470" y2="288" stroke="var(--white)" stroke-width="2"/>
  <text class="tagline" x="496" y="319" font-size="15.5" text-anchor="middle">DEALS THAT NO ONE</text>
  <text class="tagline" x="496" y="340" font-size="15.5" text-anchor="middle">CAN RESIST</text>

  <!-- product photo area -->
  <rect x="700" y="60" width="210" height="305" rx="14" fill="url(#product-tone)" role="img" aria-label="Photo of a branded white coffee mug and a white sports water bottle with a green cap"/>
</svg>
</body>
</html>
```